Re-drawing and gpahically, according to coorporate design

Three flowcharts need to be re-drawn and graphically improved according to coorporate design

```html
<!DOCTYPE html>
<html lang="en">
<head>
<meta charset="utf-8">
<title>Circular bioEconomy</title>
<link href="https://fonts.googleapis.com/css2?family=Comfortaa:wght@500;700&family=Open+Sans:wght@400;600&display=swap" rel="stylesheet">
<style>
  :root {
    --teal: #486a6a;
    --olive: #9ea41c;
    --grey: #8c8c8c;
    --grey-light: #bdbdbd;
    --ring: #c9c9c9;
    --text: #4d5f5f;
    --paper: #ffffff;
    --rule: #b9b98a;
  }
  html, body { margin: 0; padding: 0; overflow: hidden; }
  body { width: 1200px; height: 923px; background: var(--paper); }
  .poster { display: block; width: 1200px; height: 923px; }
  .title { font-family: "Comfortaa", sans-serif; font-weight: 700; font-size: 50px; fill: var(--teal); }
  .brand { font-family: "Comfortaa", sans-serif; font-weight: 700; font-size: 24px; fill: var(--teal); }
  .brand-right { font-family: "Comfortaa", sans-serif; font-weight: 700; font-size: 15px; fill: var(--grey); }
  .box-head { font-family: "Comfortaa", sans-serif; font-weight: 700; font-size: 20px; fill: #fff; letter-spacing: 0.5px; }
  .box-head-small { font-family: "Comfortaa", sans-serif; font-weight: 700; font-size: 17px; fill: #fff; letter-spacing: 0.5px; }
  .box-list { font-family: "Open Sans", sans-serif; font-size: 14px; fill: var(--text); }
  .box-list-small { font-family: "Open Sans", sans-serif; font-size: 11px; fill: var(--text); }
  .node-label { font-family: "Comfortaa", sans-serif; font-weight: 700; font-size: 13px; fill: #fff; }
  .loop-label { font-family: "Comfortaa", sans-serif; font-weight: 700; font-size: 12px; fill: var(--olive); }
  .loop-label-small { font-family: "Comfortaa", sans-serif; font-weight: 700; font-size: 11px; fill: var(--olive); }
  .flow-teal { stroke: var(--teal); stroke-width: 5.5; fill: none; }
  .flow-olive { stroke: var(--olive); stroke-width: 4; fill: none; }
  .flow-grey { stroke: var(--grey-light); stroke-width: 4.5; fill: none; }
  .box-frame { fill: #fff; stroke: var(--teal); stroke-width: 2.5; }
  .box-frame.grey { stroke: var(--grey); }
  .box-band { fill: var(--teal); }
  .box-band.grey { fill: var(--grey); }
  .node { fill: var(--teal); stroke: var(--ring); stroke-width: 4; }
  .node-grey { fill: var(--grey); stroke: #fff; stroke-width: 4; }
  .node-grey-ring { fill: none; stroke: var(--grey); stroke-width: 3; }
  .loop-box { fill: #fff; stroke: var(--olive); stroke-width: 3; }
  .funnel-teal { fill: var(--teal); }
  .funnel-grey { fill: var(--grey-light); }
</style>
</head>
<body>
<svg class="poster" viewBox="0 0 1200 923" xmlns="http://www.w3.org/2000/svg">
  <defs>
    <marker id="head-teal" viewBox="0 0 10 10" refX="8" refY="5" markerWidth="3.4" markerHeight="3.4" orient="auto">
      <path d="M0 0 L10 5 L0 10 L3 5 Z" fill="#486a6a"/>
    </marker>
    <marker id="head-olive" viewBox="0 0 10 10" refX="8" refY="5" markerWidth="4" markerHeight="4" orient="auto">
      <path d="M0 0 L10 5 L0 10 L3 5 Z" fill="#9ea41c"/>
    </marker>
    <marker id="head-grey" viewBox="0 0 10 10" refX="8" refY="5" markerWidth="3.6" markerHeight="3.6" orient="auto">
      <path d="M0 0 L10 5 L0 10 L3 5 Z" fill="#bdbdbd"/>
    </marker>
  </defs>

  <!-- header -->
  <g class="header">
    <text class="brand" x="32" y="58">Talbrook Research Centre</text>
    <text class="brand-right" x="1162" y="56" text-anchor="end">Hochschule Nordtal</text>
    <line x1="0" y1="81" x2="1200" y2="81" stroke="var(--rule)" stroke-width="1.5"/>
  </g>

  <text class="title" x="594" y="130" text-anchor="middle">Circular bioEconomy</text>

  <!-- funnels -->
  <polygon class="funnel-teal" points="714,327 818,327 764,381"/>
  <polygon class="funnel-teal" points="957,289 1116,289 1037,354"/>
  <polygon class="funnel-grey" points="156,563 86,647 235,647"/>
  <polygon class="funnel-grey" points="552,570 480,652 629,652"/>
  <polygon class="funnel-grey" points="1037,570 973,653 1116,653"/>

  <!-- grey residue flows -->
  <polyline class="flow-grey" points="207,563 300,597 300,786 318,786" marker-end="url(#head-grey)"/>
  <polyline class="flow-grey" points="513,576 445,597 445,772 424,772" marker-end="url(#head-grey)"/>
  <polyline class="flow-grey" points="370,819 370,883 765,883 765,750" marker-end="url(#head-grey)"/>

  <!-- teal main flows -->
  <line class="flow-teal" x1="208" y1="541" x2="312" y2="541" marker-end="url(#head-teal)"/>
  <line class="flow-teal" x1="418" y1="541" x2="494" y2="541" marker-end="url(#head-teal)"/>
  <line class="flow-teal" x1="604" y1="543" x2="981" y2="543" marker-end="url(#head-teal)"/>
  <line class="flow-teal" x1="563" y1="492" x2="711" y2="400" marker-end="url(#head-teal)"/>
  <line class="flow-teal" x1="815" y1="385" x2="981" y2="385" marker-end="url(#head-teal)"/>
  <line class="flow-teal" x1="601" y1="576" x2="720" y2="660" marker-end="url(#head-teal)"/>

  <!-- olive recycling loops -->
  <line class="flow-olive" x1="1069" y1="444" x2="422" y2="444"/>
  <line class="flow-olive" x1="367" y1="460" x2="367" y2="486" marker-end="url(#head-olive)"/>
  <line class="flow-olive" x1="313" y1="451" x2="196" y2="500" marker-end="url(#head-olive)"/>
  <line class="flow-olive" x1="1007" y1="432" x2="828" y2="525" marker-end="url(#head-olive)"/>
  <line class="flow-olive" x1="1069" y1="458" x2="828" y2="527" marker-end="url(#head-olive)"/>
  <line class="flow-olive" x1="712" y1="516" x2="608" y2="521" marker-end="url(#head-olive)"/>
  <polyline class="flow-olive" points="1001,583 858,630 426,630" marker-end="url(#head-olive)"/>
  <line class="flow-olive" x1="513" y1="567" x2="426" y2="640" marker-end="url(#head-olive)"/>
  <line class="flow-olive" x1="367" y1="616" x2="367" y2="594" marker-end="url(#head-olive)"/>
  <line class="flow-olive" x1="313" y1="630" x2="203" y2="585" marker-end="url(#head-olive)"/>

  <!-- info boxes -->
  <g class="info-box bioeconomy">
    <rect class="box-frame" x="42" y="143" width="227" height="161" rx="12"/>
    <rect class="box-band" x="40.75" y="141.75" width="229.5" height="54"/>
    <text class="box-head" x="155" y="176" text-anchor="middle">bioEconomy</text>
    <text class="box-list">
      <tspan x="50" y="217">• Renewability</tspan>
      <tspan x="50" y="237">• Saving fossil resources</tspan>
      <tspan x="50" y="258">• Climate friendly</tspan>
      <tspan x="50" y="278">• Improve productivity and</tspan>
      <tspan x="60" y="298">sustainability</tspan>
    </text>
  </g>

  <g class="info-box chemicals">
    <rect class="box-frame" x="649" y="143" width="236" height="184" rx="12"/>
    <rect class="box-band" x="647.75" y="141.75" width="238.5" height="56"/>
    <text class="box-head" x="767" y="166" text-anchor="middle">bioInnovation</text>
    <text class="box-head" x="767" y="190" text-anchor="middle">Chemicals</text>
    <text class="box-list">
      <tspan x="657" y="216">• innovative molecules</tspan>
      <tspan x="657" y="236">• new chemicals &amp; materials</tspan>
      <tspan x="657" y="257">• new functionalities &amp; properties</tspan>
      <tspan x="657" y="277">• more nature compatible</tspan>
      <tspan x="657" y="298">• less toxicity</tspan>
      <tspan x="657" y="318">• green &amp; sustainable chemistry</tspan>
    </text>
  </g>

  <g class="info-box products">
    <rect class="box-frame" x="924" y="143" width="232" height="146" rx="12"/>
    <rect class="box-band" x="922.75" y="141.75" width="234.5" height="56"/>
    <text class="box-head" x="1040" y="166" text-anchor="middle">bioInnovation</text>
    <text class="box-head" x="1040" y="190" text-anchor="middle">Products</text>
    <text class="box-list">
      <tspan x="930" y="216">• new functionalities &amp; properties</tspan>
      <tspan x="930" y="236">• more nature compatible</tspan>
      <tspan x="930" y="257">• new applications</tspan>
      <tspan x="930" y="277">• less toxicity</tspan>
    </text>
  </g>

  <g class="info-box farming">
    <rect class="box-frame" x="24" y="645" width="261" height="265" rx="12"/>
    <rect class="box-band" x="22.75" y="643.75" width="263.5" height="70"/>
    <text class="box-head-small" x="155" y="665" text-anchor="middle">BioInnovation</text>
    <text class="box-head-small" x="155" y="686" text-anchor="middle">Agriculture &amp; Forestry</text>
    <text class="box-head-small" x="155" y="707" text-anchor="middle">Smart Farming</text>
    <text class="box-list-small">
      <tspan x="30" y="728">• precision agriculture</tspan>
      <tspan x="30" y="743">• internet of Farm Things</tspan>
      <tspan x="30" y="758">• robotics and automation</tspan>
      <tspan x="30" y="773">• artificial intelligence</tspan>
      <tspan x="30" y="788">• soil nutrient supply</tspan>
      <tspan x="30" y="803">• soil-, plant-, and animal sensors</tspan>
      <tspan x="30" y="818">• low cost genotyping, gene editing</tspan>
      <tspan x="30" y="833">• next generation breeding</tspan>
      <tspan x="30" y="848">• microbiota in livestock and environment</tspan>
      <tspan x="30" y="863">• higher conversion efficiency: increase output</tspan>
      <tspan x="38" y="878">while reducing impact on the environment</tspan>
      <tspan x="30" y="893">• sustainable intensification</tspan>
    </text>
  </g>

  <g class="info-box processing-box">
    <rect class="box-frame grey" x="454" y="652" width="199" height="209" rx="12"/>
    <rect class="box-band grey" x="452.75" y="650.75" width="201.5" height="56"/>
    <text class="box-head-small" x="553" y="674" text-anchor="middle">bioInnovation</text>
    <text class="box-head-small" x="553" y="696" text-anchor="middle">Smart Processing</text>
    <text class="box-list-small">
      <tspan x="462" y="724">• new efficient, short pathways</tspan>
      <tspan x="462" y="740">• low energy</tspan>
      <tspan x="462" y="757">• lower toxicities</tspan>
      <tspan x="462" y="773">• elimination of harsh chemicals</tspan>
      <tspan x="462" y="789">• lower temperature</tspan>
      <tspan x="462" y="806">• lower pressure</tspan>
      <tspan x="462" y="822">• from oxidation to reduction</tspan>
      <tspan x="462" y="838">• high effeciency</tspan>
      <tspan x="462" y="855">• synthetic biology</tspan>
    </text>
  </g>

  <g class="info-box food-box">
    <rect class="box-frame" x="925" y="653" width="224" height="129" rx="12"/>
    <rect class="box-band" x="923.75" y="651.75" width="226.5" height="52"/>
    <text class="box-head-small" x="1037" y="674" text-anchor="middle">bioInnovation</text>
    <text class="box-head-small" x="1037" y="695" text-anchor="middle">Food &amp; Feed</text>
    <text class="box-list-small">
      <tspan x="931" y="724">• food quality &amp; safety</tspan>
      <tspan x="931" y="740">• functional food ingredients</tspan>
      <tspan x="931" y="757">• bioactive phytochemicals</tspan>
      <tspan x="931" y="773">• food nutrients with new functionality</tspan>
    </text>
  </g>

  <!-- recycling labels -->
  <g class="loop organic-top">
    <rect class="loop-box" x="313" y="400" width="107" height="58" rx="9"/>
    <text class="loop-label" x="367" y="424" text-anchor="middle">organic</text>
    <text class="loop-label" x="367" y="441" text-anchor="middle">recycling</text>
  </g>
  <g class="loop organic-bottom">
    <rect class="loop-box" x="313" y="616" width="107" height="61" rx="9"/>
    <text class="loop-label" x="367" y="643" text-anchor="middle">organic</text>
    <text class="loop-label" x="367" y="660" text-anchor="middle">recycling</text>
  </g>
  <g class="loop cascading">
    <rect class="loop-box" x="712" y="464" width="108" height="69" rx="9"/>
    <text class="loop-label-small" x="766" y="487" text-anchor="middle">Cascading</text>
    <text class="loop-label-small" x="766" y="501" text-anchor="middle">remanufacture</text>
    <text class="loop-label-small" x="766" y="515" text-anchor="middle">recycling</text>
  </g>
  <g class="loop share">
    <rect class="loop-box" x="1069" y="400" width="105" height="59" rx="9"/>
    <text class="loop-label-small" x="1121" y="416" text-anchor="middle">share,</text>
    <text class="loop-label-small" x="1121" y="428" text-anchor="middle">maintain,</text>
    <text class="loop-label-small" x="1121" y="440" text-anchor="middle">resuse</text>
    <text class="loop-label-small" x="1121" y="452" text-anchor="middle">redistribute</text>
  </g>

  <!-- nodes -->
  <g class="node-agriculture">
    <circle class="node" cx="156" cy="543" r="50"/>
    <text class="node-label" x="156" y="539" text-anchor="middle">agriculture</text>
    <text class="node-label" x="156" y="556" text-anchor="middle">&amp; forestry</text>
  </g>
  <g class="node-biomass">
    <circle class="node" cx="367" cy="540" r="49"/>
    <text class="node-label" x="367" y="545" text-anchor="middle">bioMass</text>
  </g>
  <g class="node-processing">
    <circle class="node-grey-ring" cx="552" cy="543" r="52"/>
    <circle class="node-grey" cx="552" cy="543" r="46"/>
    <text class="node-label" x="552" y="548" text-anchor="middle">processing</text>
  </g>
  <g class="node-chemicals">
    <circle class="node" cx="764" cy="385" r="50"/>
    <text class="node-label" x="764" y="371" text-anchor="middle">chemicals</text>
    <text class="node-label" x="764" y="388" text-anchor="middle">&amp;</text>
    <text class="node-label" x="764" y="405" text-anchor="middle">materials</text>
  </g>
  <g class="node-products">
    <circle class="node" cx="1037" cy="385" r="50"/>
    <text class="node-label" x="1037" y="381" text-anchor="middle">bio-based</text>
    <text class="node-label" x="1037" y="398" text-anchor="middle">products</text>
  </g>
  <g class="node-food">
    <circle class="node" cx="1037" cy="543" r="50"/>
    <text class="node-label" x="1037" y="539" text-anchor="middle">food &amp;</text>
    <text class="node-label" x="1037" y="556" text-anchor="middle">feed</text>
  </g>
  <g class="node-bioenergy">
    <circle class="node" cx="765" cy="694" r="50"/>
    <text class="node-label" x="765" y="690" text-anchor="middle">bioEnergy</text>
    <text class="node-label" x="765" y="707" text-anchor="middle">&amp; bioFuels</text>
  </g>
  <g class="node-residues">
    <circle class="node-grey-ring" cx="370" cy="772" r="50"/>
    <circle class="node-grey" cx="370" cy="772" r="44"/>
    <text class="node-label" x="370" y="777" text-anchor="middle">residues</text>
  </g>
</svg>
</body>
</html>
```